Sunny Paths and joy Business card

I have a logo, but will like a business card design. Is for a travel agency in Mexico. We focus in family experiences.

I will liek some thing different and unique, from the traditional business card, something to get remmeber for.

Business card information:

Leandro T. Ocampo
leandro@sunnypathsjoy.example

Alameda 482, 3 piso
Col. Tlalpizco
Mexico, D.F. 07320

office: (55) 5000-0142
mobile: (55) 9000-0187

www.sunnypathsjoy.example
@sunnypjoy
blog: sunnypathsandjoy.blogsite.example
facebook: SunnyPathsAndJoy

```html
<!DOCTYPE html>
<html lang="en">
<head>
<meta charset="utf-8">
<title>Sunny Paths and joy – Business card</title>
<link rel="stylesheet" href="https://fonts.googleapis.com/css2?family=Federo&family=Abel&display=swap">
<style>
  :root{
    --frame-yellow:#f4ee1c;
    --blue-deep:#0f6fe0;
    --blue-mid:#1f8cf2;
    --blue-light:#4fb2ff;
    --stripe-navy:#1a3a86;
    --text-white:#ffffff;
    --name-tint:#e6f3ff;
    --art-sky:#cfe9ff;
    --art-plane:#2f6fc8;
  }
  html,body{margin:0;padding:0;overflow:hidden;background:#ffffff;}
  .card{
    position:relative;width:1200px;height:686px;box-sizing:border-box;
    border:10px solid var(--frame-yellow);
    background:linear-gradient(180deg,var(--blue-deep) 0%,var(--blue-mid) 55%,var(--blue-light) 100%);
    overflow:hidden;color:var(--text-white);
  }
  .side-stripe{position:absolute;left:10px;top:0;width:14px;height:100%;background:var(--stripe-navy);}
  .person-name{
    position:absolute;left:52px;top:110px;margin:0;
    font-family:"Federo",serif;font-weight:400;font-size:62px;letter-spacing:4px;
    color:var(--name-tint);white-space:nowrap;
  }
  .website,.email{
    position:absolute;left:208px;margin:0;
    font-family:"Abel",sans-serif;white-space:nowrap;
  }
  .website{top:196px;font-size:34px;}
  .email{top:250px;font-size:28px;}
  .brand-art{position:absolute;left:770px;top:62px;width:380px;height:210px;}
  .brand-name{
    position:absolute;left:770px;top:288px;width:380px;margin:0;text-align:center;
    font-family:"Abel",sans-serif;font-size:50px;line-height:1;color:var(--text-white);
  }
  .divider{position:absolute;left:50px;top:418px;width:1080px;height:5px;background:var(--frame-yellow);}
  .address{position:absolute;left:50px;top:440px;margin:0;font-family:"Abel",sans-serif;font-style:normal;}
  .address .street{display:block;font-size:50px;line-height:62px;}
  .address .line{display:block;font-size:42px;line-height:54px;}
  .contact{position:absolute;left:768px;top:450px;margin:0;font-family:"Abel",sans-serif;}
  .contact .line{display:block;font-size:38px;line-height:50px;white-space:nowrap;}
  .contact .small{font-size:26px;line-height:38px;}
</style>
</head>
<body>
<div class="card">
  <div class="side-stripe"></div>

  <h1 class="person-name">LEANDRO T. OCAMPO</h1>
  <p class="website">www.sunnypathsjoy.example</p>
  <p class="email">leandro@sunnypathsjoy.example</p>

  <svg class="brand-art" viewBox="0 0 380 210" role="img" aria-label="Illustration of a cartoon airplane carrying two waving children among clouds">
    <defs>
      <linearGradient id="artFill" x1="0" y1="0" x2="0" y2="1">
        <stop offset="0%" stop-color="var(--art-sky)"/>
        <stop offset="100%" stop-color="var(--art-plane)"/>
      </linearGradient>
    </defs>
    <rect x="0" y="0" width="380" height="210" rx="40" fill="url(#artFill)" opacity="0.75"/>
  </svg>
  <p class="brand-name">Sunny Paths and joy</p>

  <div class="divider"></div>

  <address class="address">
    <span class="street">Alameda 482, 3 piso</span>
    <span class="line">Col. Tlalpizco&nbsp; Mexico, D.F. 07320</span>
    <span class="line">facebook: SunnyPathsAndJoy</span>
  </address>

  <p class="contact">
    <span class="line">office: (55) 5000-0142</span>
    <span class="line">mobile: (55) 9000-0187</span>
    <span class="line small">blog: sunnypathsandjoy.blogsite.example</span>
    <span class="line small">@sunnypjoy</span>
  </p>
</div>
</body>
</html>
```